Brisk Ember - Stock Certificate

We need a custom designed stock certificate that represents the look of our company logo but also have a cool look compared to a standard stock certificate. We thinking we want the logo in gold. Our website is https://www.briskemberusa.example.

We are wanting the certificate to look very professional and really cool, we have sales agents that work for the company and we are creating a program by which the sales agents can gain ownership in the company. So the certificates need to have a very cool appeal and that provides a sense of pride in owning "Units" in Brisk Ember.

Reason: Extending so other board members can vote as well, thank you all!

Target Market(s)

Stock/Shareholders

Industry/Entity Type

It Company

Font styles to use
Script

Requirements
Must have
• Must look like a stock certificate, must use our logo which the psd file for it was attached.
Nice to have
• Nice to have the logo in gold

```html
<!DOCTYPE html>
<html lang="en">
<head>
<meta charset="utf-8">
<title>Brisk Ember – Stock Certificate</title>
<link rel="stylesheet" href="https://fonts.googleapis.com/css2?family=Dancing+Script:wght@600&family=Montserrat:wght@500&display=swap">
<style>
  :root {
    --backdrop: #eef2f0;
    --paper: #fbf1d6;
    --paper-edge: #8f9c9a;
    --ornament: #b8903f;
    --frame: #9c7326;
    --ink: #4a4631;
    --rule: #8d8670;
    --seal-gold: #c9a24a;
    --seal-face: #ffffff;
    --seal-ring: #f2c21b;
    --ribbon-light: #7d6a22;
    --ribbon-dark: #6a5720;
  }
  html, body {
    margin: 0;
    width: 1200px;
    height: 917px;
    overflow: hidden;
    background: var(--backdrop);
  }
  .certificate {
    position: absolute;
    left: 20px;
    top: 45px;
    width: 1120px;
    height: 797px;
    transform: scale(1.0357);
    transform-origin: 0 0;
    background: var(--paper);
    box-shadow: 0 0 0 2px var(--paper-edge), 4px 6px 10px rgba(0,0,0,.25);
    color: var(--ink);
    font-family: "Montserrat", sans-serif;
    font-variant: small-caps;
    letter-spacing: 1px;
  }
  .certificate-art {
    position: absolute;
    inset: 0;
  }
  .title {
    position: absolute;
    left: 0;
    width: 1100px;
    top: 105px;
    margin: 0;
    text-align: center;
    font-family: "Dancing Script", cursive;
    font-variant: normal;
    font-weight: 600;
    font-size: 96px;
    letter-spacing: 0;
    line-height: 1;
    color: var(--ink);
  }
  .line-text {
    position: absolute;
    margin: 0;
    font-size: 26px;
    line-height: 1;
    white-space: nowrap;
  }
  .certify { left: 402px; top: 237px; }
  .owner { left: 257px; top: 397px; }
  .date { left: 251px; top: 470px; }
  .signed-left { left: 274px; top: 594px; }
  .signed-right { left: 857px; top: 588px; }
  .blank {
    display: inline-block;
    border-bottom: 1.5px solid var(--ink);
    vertical-align: baseline;
    margin: 0 18px;
    height: 0;
  }
  .seal-name {
    position: absolute;
    left: 507px;
    width: 110px;
    top: 684px;
    margin: 0;
    text-align: center;
    font-size: 13px;
    line-height: 1;
    font-variant: normal;
    letter-spacing: .5px;
    color: var(--ink);
  }
</style>
</head>
<body>
  <main class="certificate">
    <svg class="certificate-art" width="1120" height="797" viewBox="0 0 1120 797">
      <defs>
        <linearGradient id="ribbon-tone" x1="0" y1="0" x2="0" y2="1">
          <stop offset="0" stop-color="var(--ribbon-light)"/>
          <stop offset="1" stop-color="var(--ribbon-dark)"/>
        </linearGradient>
      </defs>
      <path class="ornament-band" role="img" aria-label="Ornamental scrollwork border"
            fill="var(--ornament)" fill-opacity=".55" fill-rule="evenodd"
            d="M18 22H1102V778H18Z M58 68H1062V735H58Z"/>
      <rect class="outer-frame" x="64" y="72" width="992" height="658" fill="var(--paper)" stroke="var(--frame)" stroke-width="6"/>
      <rect class="inner-frame" x="76" y="84" width="968" height="634" fill="none" stroke="var(--frame)" stroke-width="2"/>
      <line class="name-rule" x1="200" y1="341" x2="916" y2="341" stroke="var(--rule)" stroke-width="1"/>
      <line class="signature-rule" x1="152" y1="620" x2="260" y2="620" stroke="var(--ink)" stroke-width="1.5"/>
      <line class="signature-rule" x1="735" y1="614" x2="842" y2="614" stroke="var(--ink)" stroke-width="1.5"/>
      <rect class="ribbon-area" role="img" aria-label="Decorative ribbon banner behind the seal"
            x="295" y="688" width="525" height="56" fill="url(#ribbon-tone)"/>
      <circle class="seal-rim" cx="562" cy="685" r="90" fill="var(--seal-gold)"/>
      <circle class="seal-ring" cx="562" cy="685" r="68" fill="var(--seal-ring)"/>
      <circle class="seal-face" cx="562" cy="685" r="62" fill="var(--seal-face)"/>
      <circle class="seal-dot" cx="562" cy="665" r="9" fill="var(--seal-gold)"/>
    </svg>

    <h1 class="title">Stock Certificate</h1>
    <p class="line-text certify">This is to certify that</p>
    <p class="line-text owner">Is the OWNER of<span class="blank" style="width:92px"></span>shares of stock</p>
    <p class="line-text date"><span class="blank" style="width:60px;margin-left:0"></span>On this<span class="blank" style="width:76px"></span>Day of<span class="blank" style="width:76px"></span>In the year</p>
    <p class="line-text signed-left">Signed</p>
    <p class="line-text signed-right">Signed</p>
    <p class="seal-name">Brisk Ember</p>
  </main>
</body>
</html>
```